A Cool Business Card so My Son can Network with People, Especially People in the Entertainment Business. Something that stands out and;Pops:*) He's an Entertainer goes by the ☆Kelso Dune KD Please include His Social Media that you will see and Contact Numbers as well in the pics. Submitted Please Hook It Up. Thanks!

Contact Information for Business Card:

A Cool Hip-hop ,Entertainer Design for My 16 Year old Son. He Sings,Raps,Actor,Dancer and Radio Personality as well. Something that stands out from the rest of the Business Cards & Pops. He's A Star Already it's only a matter of Time Until He Becomes A Superstar.

Thank You For Your Help!

Target Market(s)

18-40 y/o

Industry/Entity Type

Entertainment Industry

Contact Information for Business Card

To promote my artistry to the public
Im a Singer,Rapper,Dancer,Actor&Model

Font styles to use
Serif

Requirements
Must have
• artist name- Kelso Dune KD
• social media connections
• which are on the pics. downloaded.
Nice to have
• *Kelso Dune* KD
• Social Media Info as well as cell phone info located in downloads:*}
• Make it pop,add some of the Pics. Be Creative He is a Future Superstar:*)
Should not have
• Make it Amazing But also readable for His important info But make the Card off the chain any colors dont make it Girly He is a 16 year old Teenager. I left enough downloads of Pics. that someone who is Creative can make something Wonderful. Then whoever that is will work with Us on other Projects Including makin a CD Cover:.)

```html
<!DOCTYPE html>
<html lang="en">
<head>
<meta charset="utf-8">
<title>Kelso Dune KD — Business Card</title>
<link rel="stylesheet" href="https://fonts.googleapis.com/css2?family=Lato:wght@300;400;700;900&family=Cabin+Condensed:wght@400;500&display=swap">
<style>
  :root {
    --stage: #6a6a6a;
    --card-black: #000000;
    --card-pink: #c9559f;
    --pink-light: #de8cc4;
    --pink-mid: #d170b3;
    --pink-deep: #b8458d;
    --white: #ffffff;
    --edge: #8a8a8a;
  }
  * { margin: 0; padding: 0; box-sizing: border-box; }
  html, body {
    width: 1200px; height: 946px; overflow: hidden;
    background: var(--stage);
  }
  .canvas { position: relative; width: 1200px; height: 946px; }

  /* Front: contact side */
  .card-front {
    position: absolute; left: 0; top: 0; width: 566px; height: 946px;
    background: var(--card-black); color: var(--white);
  }
  .artist-name {
    position: absolute; left: 66px; top: 88px;
    font-family: "Lato", sans-serif; font-size: 60px; line-height: 1;
    letter-spacing: 1px; font-weight: 300;
  }
  .artist-name strong { font-weight: 700; }
  .roles {
    position: absolute; left: 68px; top: 162px;
    font-family: "Cabin Condensed", sans-serif; font-size: 23px;
    word-spacing: 10px; letter-spacing: 0.3px;
  }
  .contact-row {
    position: absolute; left: 66px; display: flex; align-items: center; gap: 8px;
    font-family: "Cabin Condensed", sans-serif; font-size: 32px; line-height: 1.05;
  }
  .contact-row .icon { width: 54px; height: 46px; flex: none; }
  .contact-row .mark {
    width: 50px; height: 50px; flex: none; border: 4px solid var(--white); border-radius: 50%;
  }
  .contact-row .mark.square { border-radius: 6px; }
  .row-phone { top: 378px; }
  .row-email { top: 474px; }
  .row-social { top: 548px; }
  .row-audio { top: 630px; }
  .row-video { top: 710px; }

  /* Back: photo side */
  .card-back {
    position: absolute; left: 637px; top: 0; width: 561px; height: 944px;
    background: var(--card-pink); border: 1px solid var(--edge);
  }
  .photo-area {
    position: absolute; left: 10px; top: 72px; width: 522px; height: 798px;
    background:
      radial-gradient(ellipse at 30% 25%, var(--pink-light), transparent 60%),
      radial-gradient(ellipse at 75% 70%, var(--pink-light), transparent 55%),
      linear-gradient(160deg, var(--pink-mid), var(--pink-deep));
    opacity: 0.9;
  }
  .vertical-name {
    position: absolute; left: 281px; top: 460px;
    transform: translate(-50%, -50%) rotate(-90deg);
    font-family: "Lato", sans-serif; font-size: 68px; line-height: 1;
    color: var(--white); font-weight: 300; letter-spacing: 2px; white-space: nowrap;
  }
  .vertical-name strong { font-weight: 700; }
</style>
</head>
<body>
<div class="canvas">
  <section class="card-front">
    <h1 class="artist-name">KELSO<strong>DUNE</strong></h1>
    <p class="roles">Singer Rapper Dancer Actor Model</p>

    <div class="contact-row row-phone">
      <svg class="icon" viewBox="0 0 54 46" fill="none" stroke="#fff" stroke-width="3.5">
        <path d="M4 16 C4 6 50 6 50 16 L50 20 L38 20 L38 14 L16 14 L16 20 L4 20 Z"/>
        <rect x="8" y="22" width="38" height="21" rx="3"/>
        <circle cx="27" cy="32" r="6"/>
      </svg>
      <div>555-014-2710<br>555-014-8832</div>
    </div>

    <div class="contact-row row-email">
      <svg class="icon" viewBox="0 0 54 46" fill="none" stroke="#fff" stroke-width="3.5">
        <rect x="3" y="7" width="48" height="32" rx="2"/>
        <path d="M3 9 L27 27 L51 9"/>
      </svg>
      <span>KelsoDunemania@Mailbox.com</span>
    </div>

    <div class="contact-row row-social">
      <span class="mark square"></span>
      <span>@therealkelsodunekd</span>
    </div>

    <div class="contact-row row-audio">
      <span class="mark"></span>
      <span>KelsoDuneKD</span>
    </div>

    <div class="contact-row row-video">
      <span class="mark square"></span>
      <span>KelsoDuneKD</span>
    </div>
  </section>

  <section class="card-back">
    <div class="photo-area" role="img" aria-label="Collage of portrait photos of the artist arranged inside a large X shape, tinted pink"></div>
    <h2 class="vertical-name">KELSO<strong>DUNE</strong></h2>
  </section>
</div>
</body>
</html>
```